Velmarcoteni Business cards

Dear team, I need to get the design file to suit it to our team. The focus of the business card is the Automotive Market and the design must be in black colour and the logo must be in glossy black. On the front of the card I need to get the following info:

- Name and Surname
- Title
- eMail
- Phone Number
- Skype account
- domain address

```html
<!DOCTYPE html>
<html lang="en">
<head>
<meta charset="utf-8">
<title>Velmarcoteni Business Cards</title>
<link rel="stylesheet" href="https://fonts.googleapis.com/css2?family=Archivo:wght@400;700&family=Oswald:wght@600&display=swap">
<style>
  :root {
    --stage: #d9d9d9;
    --card: #1b1b1c;
    --card-back: #161617;
    --gloss: #262628;
    --red: #ee2a31;
    --white: #ffffff;
    --muted: #e8e8e8;
  }
  * { margin: 0; padding: 0; box-sizing: border-box; }
  html, body { width: 1200px; height: 912px; overflow: hidden; background: var(--stage); }
  .canvas { position: relative; width: 1200px; height: 912px; }
  .card {
    position: absolute; width: 640px; height: 366px; overflow: hidden;
    box-shadow: 0 10px 24px rgba(0,0,0,.25);
  }
  .card--back { left: 120px; top: 60px; background: var(--card-back); }
  .card--front { left: 440px; top: 486px; background: var(--card); }

  .back-mark {
    position: absolute; inset: 0; display: flex; align-items: center; justify-content: center;
    font: 700 64px/1 "Archivo", sans-serif; color: var(--gloss); letter-spacing: -1px;
  }

  .card-art { position: absolute; inset: 0; }

  .brand {
    position: absolute; left: 40px; top: 50px; display: flex; align-items: center; gap: 12px;
  }
  .brand-square { width: 32px; height: 32px; background: var(--red); }
  .brand-name { font: 700 34px/1 "Archivo", sans-serif; color: var(--white); letter-spacing: -0.5px; }

  .person { position: absolute; right: 40px; top: 126px; text-align: right; }
  .person-name { font: 600 32px/1 "Oswald", sans-serif; color: var(--red); text-transform: uppercase; letter-spacing: .5px; }
  .person-title { font: 400 16px/1.3 "Archivo", sans-serif; color: var(--white); margin-top: 2px; }

  .contacts { position: absolute; right: 40px; top: 202px; list-style: none; text-align: right; }
  .contacts li {
    display: flex; justify-content: flex-end; align-items: center; gap: 7px;
    font: 400 15px/21px "Archivo", sans-serif; color: var(--muted);
  }
  .contacts svg { width: 11px; height: 11px; flex: none; }

  .address {
    position: absolute; left: 40px; top: 250px; font-style: normal;
    font: 400 17px/1.35 "Archivo", sans-serif; color: var(--white);
  }
</style>
</head>
<body>
<main class="canvas">

  <section class="card card--back" aria-label="Card back">
    <div class="back-mark">Velmarcoteni</div>
  </section>

  <section class="card card--front" aria-label="Card front">
    <svg class="card-art" width="640" height="366" viewBox="0 0 640 366" aria-hidden="true">
      <line x1="40" y1="194" x2="600" y2="194" stroke="var(--red)" stroke-width="1.5"/>
      <path d="M372 304 L394 292 L640 292 L640 280 L390 280 Z" fill="var(--white)"/>
      <path d="M0 366 L0 336 L300 336 C340 336 360 310 400 308 L640 298 L640 366 Z" fill="var(--red)"/>
    </svg>

    <div class="brand">
      <span class="brand-square"></span>
      <span class="brand-name">Velmarcoteni</span>
    </div>

    <div class="person">
      <div class="person-name">Orlan Dravik</div>
      <div class="person-title">Director</div>
    </div>

    <ul class="contacts">
      <li>555-014-2287
        <svg viewBox="0 0 12 12"><path d="M2.5 1 L4.5 1 L5.2 3.6 L4 4.6 C4.7 6 6 7.3 7.4 8 L8.4 6.8 L11 7.5 L11 9.5 C11 10.3 10.3 11 9.5 11 C5 11 1 7 1 2.5 C1 1.7 1.7 1 2.5 1 Z" fill="var(--red)"/></svg>
      </li>
      <li>info@velmarcoteni.com
        <svg viewBox="0 0 12 12"><rect x="1" y="2.5" width="10" height="7" fill="var(--red)"/><path d="M1 2.5 L6 6.5 L11 2.5" stroke="var(--card)" stroke-width="1" fill="none"/></svg>
      </li>
      <li>velmarcoteni
        <svg viewBox="0 0 12 12"><circle cx="6" cy="6" r="5" fill="none" stroke="var(--red)" stroke-width="1.6"/></svg>
      </li>
    </ul>

    <address class="address">2280 W Calder Row, Brennford,<br>Ohio 40219</address>
  </section>

</main>
</body>
</html>
```